KB Rubbish Removal Business Card

Hey,
I need a double sided business card designed for a rubbish removal business based in Australia. Logo is already chosen, similar colours preferred for both sides of the business card.

Details to include:

Front:

KB Rubbish Removal
Darren Holloway
Managing Director
Mobile: 0471 902 146
Email: darren@kbrubbishremoval.com.au
Website: kbrubbishremoval.com.au

Rear:

How did we do?
kbrubbishremoval.com.au/review

```html
<!DOCTYPE html>
<html lang="en">
<head>
<meta charset="utf-8">
<title>KB Rubbish Removal – Business Card</title>
<link rel="stylesheet" href="https://fonts.googleapis.com/css2?family=Montserrat:wght@300;400;700&display=swap">
<style>
  :root {
    --stage: #000000;
    --paper: #ffffff;
    --brand-dark: #2e6e2a;
    --brand-mid: #3aa845;
    --grass: #00b140;
    --lime: #a4d93e;
    --ink: #555555;
    --white: #ffffff;
  }
  * { margin: 0; padding: 0; box-sizing: border-box; }
  html, body {
    width: 1122px; height: 1200px; overflow: hidden;
    background: var(--stage);
    font-family: "Montserrat", sans-serif;
  }
  .canvas { position: relative; width: 1122px; height: 1200px; }

  .card { position: absolute; left: 134px; width: 860px; height: 492px; overflow: hidden; }

  /* Front */
  .card--front { top: 71px; background: var(--paper); }
  .brand-mark {
    position: absolute; left: 521px; top: 56px;
    width: 100px; height: 100px; border-radius: 50%;
    background: linear-gradient(135deg, var(--brand-mid), var(--brand-dark));
  }
  .company-name {
    position: absolute; left: 0; right: 0; top: 198px;
    text-align: center; padding-left: 30px;
    font-weight: 700; font-size: 48px; color: var(--brand-dark);
    letter-spacing: 0.2px;
  }
  .person { position: absolute; right: 508px; top: 372px - 71px; text-align: right; }
  .person__name {
    position: absolute; right: 508px; top: 302px; white-space: nowrap;
    font-weight: 700; font-size: 31px; color: var(--ink);
  }
  .person__role {
    position: absolute; right: 508px; top: 358px; white-space: nowrap;
    font-weight: 300; font-size: 22px; color: var(--ink); letter-spacing: 0.5px;
  }
  .divider {
    position: absolute; left: 380px; top: 310px; width: 1px; height: 78px;
    background: var(--brand-mid);
  }
  .contact { position: absolute; left: 407px; top: 305px; list-style: none; }
  .contact__item {
    display: flex; align-items: center; height: 30px; margin-bottom: 1px;
    font-size: 19px; color: var(--ink); letter-spacing: 0.3px;
  }
  .contact__item:last-child { margin-top: 2px; }
  .contact__icon { width: 20px; height: 20px; margin-right: 34px; fill: var(--brand-dark); flex: none; }

  /* Back */
  .card--back {
    top: 608px;
    background: linear-gradient(225deg, var(--lime) 0%, #5cc847 30%, #1fb544 55%, var(--grass) 80%);
  }
  .review__title {
    position: absolute; left: 0; right: 0; top: 198px; text-align: center;
    font-weight: 700; font-size: 41px; color: var(--white);
  }
  .review__link {
    position: absolute; left: 0; right: 0; top: 257px; text-align: center;
    font-weight: 300; font-size: 28px; color: rgba(255,255,255,0.75);
  }
</style>
</head>
<body>
<main class="canvas">
  <section class="card card--front" aria-label="Card front">
    <div class="brand-mark" aria-hidden="true"></div>
    <h1 class="company-name">KB Rubbish Removal</h1>
    <p class="person__name">Darren Holloway</p>
    <p class="person__role">Managing Director</p>
    <div class="divider"></div>
    <ul class="contact">
      <li class="contact__item">
        <svg class="contact__icon" viewBox="0 0 24 24" aria-hidden="true"><path d="M6.6 10.8a15.1 15.1 0 0 0 6.6 6.6l2.2-2.2a1 1 0 0 1 1-.25 11.4 11.4 0 0 0 3.6.57 1 1 0 0 1 1 1V20a1 1 0 0 1-1 1A17 17 0 0 1 3 4a1 1 0 0 1 1-1h3.5a1 1 0 0 1 1 1c0 1.25.2 2.45.57 3.57a1 1 0 0 1-.25 1z"/></svg>
        0471 902 146
      </li>
      <li class="contact__item">
        <svg class="contact__icon" viewBox="0 0 24 24" aria-hidden="true"><path d="M12 2a10 10 0 1 0 5 18.7l-1-1.7A8 8 0 1 1 20 12v1.2a1.8 1.8 0 0 1-3.6 0V7.5h-2v.9A4.6 4.6 0 1 0 15 15.7a3.8 3.8 0 0 0 7-2.5V12A10 10 0 0 0 12 2zm0 12.6a2.6 2.6 0 1 1 0-5.2 2.6 2.6 0 0 1 0 5.2z"/></svg>
        darren@kbrubbishremoval.com.au
      </li>
      <li class="contact__item">
        <svg class="contact__icon" viewBox="0 0 24 24" aria-hidden="true"><path d="M12 2a10 10 0 1 0 0 20 10 10 0 0 0 0-20zm-1 2.1V8H7.4A8 8 0 0 1 11 4.1zM13 4.1A8 8 0 0 1 16.6 8H13zM4.3 10H11v4H4.3a8 8 0 0 1 0-4zM13 10h6.7a8 8 0 0 1 0 4H13zM7.4 16H11v3.9A8 8 0 0 1 7.4 16zM13 16h3.6A8 8 0 0 1 13 19.9z"/></svg>
        kbrubbishremoval.com.au
      </li>
    </ul>
  </section>

  <section class="card card--back" aria-label="Card back">
    <h2 class="review__title">How did we do?</h2>
    <p class="review__link">kbrubbishremoval.com.au/review</p>
  </section>
</main>
</body>
</html>
```